Quill And Ferry Business Card

I need a business card designed around my logo (which was designed here on Sketch Forum!)

Target Market(s)

Professional Businesses

Industry/Entity Type

Business

Requirements
Must have
• Details that must be on the business card:

Renata Ovalle
Director
0491 253 608
renata@quillandferry.com.au
www.quillandferry.com.au
PO Box 4720 Harlow Bay Vic 3981

```html
<!DOCTYPE html>
<html lang="en">
<head>
<meta charset="utf-8">
<title>Quill And Ferry Business Card</title>
<link href="https://fonts.googleapis.com/css2?family=Cinzel:wght@400;600&family=Open+Sans:wght@400;600&display=swap" rel="stylesheet">
<style>
  :root {
    --backdrop: #e9e6e2;
    --card: #ffffff;
    --ink: #1e1e1e;
    --red: #c8232b;
    --red-dark: #9e1a20;
    --shadow: rgba(0, 0, 0, 0.18);
  }
  html, body {
    margin: 0;
    padding: 0;
    width: 1200px;
    height: 1000px;
    overflow: hidden;
    background: var(--backdrop);
  }
  .stage {
    position: relative;
    width: 1200px;
    height: 1000px;
  }
  .card {
    position: absolute;
    width: 600px;
    height: 330px;
    background: var(--card);
    box-shadow: 0 6px 20px var(--shadow);
    overflow: hidden;
  }
  .card--front { left: 60px; top: 150px; }
  .card--back { left: 540px; top: 520px; }

  .brand {
    position: absolute;
    display: flex;
    align-items: center;
    gap: 18px;
  }
  .brand__square {
    width: 62px;
    height: 62px;
    background: var(--red);
    flex: none;
  }
  .brand__name {
    font-family: "Cinzel", serif;
    font-weight: 400;
    color: var(--ink);
    font-size: 38px;
    letter-spacing: 0.5px;
    line-height: 1;
    white-space: nowrap;
  }
  .card--front .brand { left: 64px; top: 134px; }

  .web-band {
    position: absolute;
    right: 0;
    bottom: 24px;
    width: 258px;
    height: 32px;
    background: linear-gradient(#d12a31, var(--red-dark));
    color: #fff;
    font-family: "Cinzel", serif;
    font-size: 14px;
    letter-spacing: 0.4px;
    display: flex;
    align-items: center;
    justify-content: center;
  }

  .person {
    position: absolute;
    left: 16px;
    top: 50px;
    font-family: "Open Sans", sans-serif;
  }
  .person__name {
    margin: 0;
    font-size: 25px;
    font-weight: 400;
    color: var(--ink);
  }
  .person__role {
    margin: 2px 0 0;
    font-size: 9px;
    font-weight: 600;
    letter-spacing: 1px;
    text-transform: uppercase;
    color: var(--red);
  }
  .contact {
    position: absolute;
    left: 16px;
    top: 142px;
    margin: 0;
    padding: 0;
    list-style: none;
    font-family: "Open Sans", sans-serif;
    font-size: 16px;
    line-height: 22px;
    color: var(--ink);
  }
  .contact__label { color: var(--red); }
  .address {
    position: absolute;
    left: 16px;
    top: 254px;
    margin: 0;
    font-family: "Open Sans", sans-serif;
    font-size: 16px;
    color: var(--ink);
  }
  .card--back .brand {
    right: 26px;
    top: 272px;
    gap: 8px;
  }
  .card--back .brand__square { width: 28px; height: 28px; }
  .card--back .brand__name { font-size: 17px; }
</style>
</head>
<body>
  <main class="stage">
    <section class="card card--front" aria-label="Card front">
      <div class="brand">
        <span class="brand__square"></span>
        <span class="brand__name">QUILL AND FERRY</span>
      </div>
      <div class="web-band">WWW.QUILLANDFERRY.COM.AU</div>
    </section>

    <section class="card card--back" aria-label="Card back">
      <div class="person">
        <h1 class="person__name">Renata Ovalle</h1>
        <p class="person__role">Director</p>
      </div>
      <ul class="contact">
        <li><span class="contact__label">t:</span> 0491 253 608</li>
        <li><span class="contact__label">e:</span> renata@quillandferry.com.au</li>
        <li><span class="contact__label">w:</span> www.quillandferry.com.au</li>
      </ul>
      <p class="address">PO Box 4720 Harlow Bay Vic 3981</p>
      <div class="brand">
        <span class="brand__square"></span>
        <span class="brand__name">QUILL AND FERRY</span>
      </div>
    </section>
  </main>
</body>
</html>
```